PEACFUL ACUPUNCTURE PRACTITIONER NEEDS A NEW COAT

I need a new design for an exiting website http://willowgateneedlework.com/ for a acupuncturist. This will be a minimalism design with lots and lots of white space. Home page and one interior page. Please keep the feeling of calm and peaceful serenity. For Color scheme: https://www.morningfernclinic.com/fertility. The bottom part of the home page with sections and links to the service pages: https://harborlotuswellness.com/. The client likes this the best: http://mfclinic.com/. I'm attaching the logo and content pages.

Target Market(s)

Women

Industry/Entity Type

Wellness, health, wellbeing, meditation

Number of Pages Required

2 page

Font styles to use
Sans Serif
Decorative

Colors

Designer to choose colors to be used in the design.

Requirements
Must have
Nice to have
• Follow new website drafts and links
Should not have
• Busy with bright colors. No poping

```html
<!DOCTYPE html>
<html lang="en">
<head>
<meta charset="utf-8">
<title>Willowgate Acupuncture</title>
<link rel="stylesheet" href="https://fonts.googleapis.com/css2?family=Della+Respira&family=Poppins:wght@300;400;500;600&display=swap">
<style>
:root{
  --page:#e6c2c6;
  --rose:#c4939a;
  --rose-soft:#c9969c;
  --ink:#1f1f22;
  --text:#4a4a4a;
  --muted:#6d6d6d;
  --white:#ffffff;
  --line:#ececec;
  --footer:#1e1e20;
  --footer-deep:#161618;
}
*{box-sizing:border-box;margin:0;padding:0}
html,body{width:1200px;height:2820px;overflow:hidden}
body{background:var(--page);font-family:"Poppins",sans-serif;color:var(--text)}
.site{position:absolute;left:192px;top:0;width:816px;height:2820px;background:var(--white)}
.serif{font-family:"Della Respira",serif;font-weight:400}

/* header */
.topbar{position:relative;height:122px;border-bottom:1px solid var(--line)}
.contact-lines{position:absolute;left:78px;top:50px;font-size:9px;color:var(--muted);line-height:19px}
.contact-lines div{display:flex;align-items:center;gap:10px}
.contact-lines svg{width:13px;height:13px}
.brand{position:absolute;left:0;right:0;top:26px;text-align:center;color:var(--rose)}
.brand-dot{width:40px;height:40px;border-radius:50%;background:var(--rose);opacity:.75;margin:0 auto 4px}
.brand-name{font-family:"Della Respira",serif;font-size:19px;line-height:20px;color:#7a6a6c}
.brand-sub{font-size:9px;letter-spacing:2.5px;color:var(--rose)}
.socials{position:absolute;right:83px;top:62px;display:flex;gap:5px}
.socials span{width:16px;height:16px;border-radius:50%;background:var(--rose)}

.nav{position:relative;height:58px;display:flex;justify-content:center;gap:0;padding-left:4px}
.nav a{font-size:8.3px;color:#555;text-decoration:none;text-transform:uppercase;padding:20px 12px 0;position:relative}
.nav a.active{color:var(--rose)}
.nav a.active::before{content:"";position:absolute;left:12px;right:12px;top:0;height:1px;background:var(--rose)}

/* hero */
.hero{position:relative;height:372px;background:linear-gradient(100deg,#3b3134 0%,#6e5551 35%,#8b7068 55%,#5a5150 100%);text-align:center;color:var(--white)}
.hero h1{font-family:"Della Respira",serif;font-weight:400;font-size:74px;letter-spacing:1px;padding-top:110px;line-height:74px}
.hero .rule{width:104px;height:3px;background:var(--rose);margin:20px auto 18px}
.hero p{font-size:14.5px;line-height:21px;width:420px;margin:0 auto}

/* philosophy */
.philosophy{height:440px;text-align:center}
.section-title{font-size:40px;color:var(--ink);line-height:44px}
.philosophy .section-title{padding-top:76px}
.lede{font-size:8.3px;line-height:14px;color:#666;width:430px;margin:20px auto 0}
.pillars{display:flex;justify-content:center;margin-top:38px}
.pillar{width:170px;height:152px;padding:0 20px}
.pillar + .pillar{border-left:1px solid var(--rose)}
.pillar .icon{width:58px;height:58px;border-radius:50%;margin:0 auto 14px;display:flex;align-items:center;justify-content:center}
.pillar .icon.rose{background:var(--rose)}
.pillar .icon.dark{background:var(--ink)}
.pillar .icon span{width:22px;height:22px;border-radius:50%;background:var(--white)}
.pillar h3{font-size:11px;font-weight:500;color:var(--ink);line-height:14px;height:28px}
.pillar p{font-size:8.3px;line-height:14px;color:#666;margin-top:16px}

/* about */
.about{position:relative;height:431px;background:linear-gradient(90deg,#c28f97 0%,#cc9ea4 50%,#c4959b 100%);text-align:center;color:var(--white)}
.portrait{width:74px;height:74px;border-radius:50%;border:3px solid var(--white);background:linear-gradient(#e4b79d,#b77f6f);margin:0 auto;position:relative;top:42px}
.about h2{font-size:66px;line-height:70px;padding-top:60px}
.about p{font-size:12.3px;line-height:21px;width:650px;margin:22px auto 0}
.about p + p{margin-top:21px}

/* testimonials */
.testimonials{height:524px;text-align:center}
.testimonials .section-title{padding-top:78px}
.cards{display:flex;justify-content:center;gap:38px;margin-top:42px}
.card{position:relative;width:303px;height:193px;background:var(--white);box-shadow:0 4px 22px rgba(0,0,0,.13)}
.avatar{position:absolute;left:50%;top:-34px;margin-left:-34px;width:68px;height:68px;border-radius:50%;border:2px solid var(--rose);background:linear-gradient(#8a6a5e,#3e2e2a)}
.card blockquote{font-size:8.3px;font-style:italic;line-height:14px;color:#666;width:225px;margin:60px auto 0}
.card .who{font-size:10px;color:var(--rose);margin-top:16px}
.card .role{font-size:7.5px;font-weight:600;color:var(--ink);margin-top:4px}
.card .quote-mark{position:absolute;left:26px;top:142px;font-family:"Della Respira",serif;font-size:46px;color:var(--rose);line-height:46px}

/* contact */
.contact{position:relative;height:572px;background:linear-gradient(120deg,#c79aa0 0%,#cfa4a8 60%,#c3969b 100%);text-align:center;color:var(--white)}
.contact h2{font-size:40px;line-height:44px;padding-top:64px}
.contact .lede{color:var(--white);margin-top:24px}
.map{position:absolute;left:92px;top:200px;width:306px;height:290px;background:linear-gradient(135deg,#eef0ec,#dfe6dd 60%,#e9ece6)}
.form{position:absolute;left:461px;top:200px;width:273px;text-align:left}
.field{height:35px;border:1.5px solid var(--white);color:var(--white);font-size:11px;padding:9px 18px;margin-bottom:16px}
.field.message{height:81px}
.submit{display:inline-block;width:124px;height:34px;background:var(--white);color:var(--ink);font-size:12.5px;font-weight:600;text-align:center;line-height:34px;margin-top:7px}

/* footer */
.footer{position:relative;height:251px;background:var(--footer);color:var(--white)}
.footer .logo{position:absolute;left:87px;top:52px;display:flex;align-items:center;gap:8px}
.footer .logo-dot{width:44px;height:44px;border-radius:50%;background:var(--rose);opacity:.8}
.footer .logo-name{font-family:"Della Respira",serif;font-size:25px;line-height:24px}
.footer .logo-sub{font-size:12px;letter-spacing:3px}
.footer .about-text{position:absolute;left:87px;top:116px;width:250px;font-size:9px;line-height:14px}
.footer .socials{right:auto;left:87px;top:194px}
.footer .socials span{width:15px;height:15px}
.col{position:absolute;top:72px;font-size:9px;line-height:14px}
.col h4{font-size:10.5px;font-weight:600;margin-bottom:16px}
.col.contact-col{left:383px;width:160px}
.col.consult-col{left:558px;width:175px}
.row{display:flex;gap:8px;margin-bottom:20px}
.row svg{width:8px;height:10px;flex:none;margin-top:2px}
.col a{color:var(--rose);text-decoration:none;display:block;margin-top:14px}
.copyright{position:absolute;left:0;right:0;bottom:0;height:50px;background:var(--footer-deep);color:var(--white);font-size:9px;text-align:center;line-height:50px}
</style>
</head>
<body>
<div class="site">
  <header class="topbar">
    <div class="contact-lines">
      <div><svg viewBox="0 0 16 16"><path fill="#c4939a" d="M3 1l3 3-1.5 2c1 2 3 4 5 5l2-1.5 3 3-2 2C7 14 2 9 1 3z"/></svg>413-555-0142</div>
      <div><svg viewBox="0 0 16 16"><rect x="1" y="3" width="14" height="10" fill="#c4939a"/><path d="M1 3l7 6 7-6" stroke="#fff" stroke-width="1.2" fill="none"/></svg>maren@willowgateneedlework.com</div>
    </div>
    <div class="brand">
      <div class="brand-dot"></div>
      <div class="brand-name">Willowgate</div>
      <div class="brand-sub">ACUPUNCTURE</div>
    </div>
    <div class="socials"><span></span><span></span><span></span></div>
  </header>
  <nav class="nav">
    <a class="active">Home</a><a>About Maren</a><a>Treatments</a><a>Health Concerns</a><a>Fertility</a><a>Pregnancy</a><a>Questions</a><a>Shop</a><a>Testimonial</a><a>Contact</a>
  </nav>

  <section class="hero" role="img" aria-label="Photo of a woman relaxing during a shoulder massage">
    <h1>ACUPUNCTURE</h1>
    <div class="rule"></div>
    <p>Acupuncture &amp; Chinese Herbal Medicine are rooted in over 3000 years of history and tradition.</p>
  </section>

  <section class="philosophy">
    <h2 class="section-title serif">Philosophy of Care</h2>
    <p class="lede">Acupuncture &amp; Chinese Herbal Medicine are rooted in over 3000 years of history and tradition. As a complete medical system that has remained flexible and relevant we honor what has worked from the past while embracing the medicine of tomorrow.</p>
    <div class="pillars">
      <div class="pillar"><div class="icon rose"><span></span></div><h3>Fertility &amp;<br>Pregnancy</h3><p>At Willowgate Acupuncture our goal is to help</p></div>
      <div class="pillar"><div class="icon dark"><span></span></div><h3>Emotional Well<br>Being</h3><p>Our mental and emotional wellness is imperative</p></div>
      <div class="pillar"><div class="icon rose"><span></span></div><h3>Hormone<br>Balance</h3><p>Our hormones are constantly shifting</p></div>
      <div class="pillar"><div class="icon dark"><span></span></div><h3>Strength &amp;<br>Structure</h3><p>Our bodies carry us through all we do. Sometimes</p></div>
    </div>
  </section>

  <section class="about" role="img" aria-label="Rose-tinted photo of two smiling women outdoors">
    <div class="portrait" role="img" aria-label="Portrait of the practitioner"></div>
    <h2 class="serif">About Maren</h2>
    <p>Maren Holloway is a Massachusetts and California Licensed Acupuncturist and Herbalist as Degree from Silver Pine University in Santa Cruz CA &nbsp;and has studied at the integrated hospital in Hang Zhou China. She has also done extensive study in Chi Nei Tsang in both the USA and Thailand.</p>
    <p>She worked for Tallgrass Herb Company a leader of high quality, lab tested Chinese patented herbal formulas as a consultant to both Acupuncturists and Western MD's. Every year Maren commits to attending in person and virtual educational events in order to grow as a practitioner and human being.</p>
  </section>

  <section class="testimonials">
    <h2 class="section-title serif">Testimonials</h2>
    <p class="lede">Acupuncture &amp; Chinese Herbal Medicine are rooted in over 3000 years of history and tradition. As a complete medical system that has remained flexible</p>
    <div class="cards">
      <div class="card">
        <div class="avatar" role="img" aria-label="Client portrait"></div>
        <blockquote>" Maren is such an incredibly skilled, competent and knowledgeable practitioner. I started seeing Maren because after a year and a half of trying to conceive, and suffering a miscarriage along the way</blockquote>
        <div class="who">C Baby Born 2017</div>
        <div class="role">CLIENT</div>
        <div class="quote-mark">“</div>
      </div>
      <div class="card">
        <div class="avatar" role="img" aria-label="Client portrait"></div>
        <blockquote>" When I first came to Maren's office I was very desperate and pretty hopeless. &nbsp;I had been trying to conceive for close to three years and had had 4 failed IUIs and 3 failed IVFs with the final one resulting</blockquote>
        <div class="who">L</div>
        <div class="role">CLIENT</div>
        <div class="quote-mark">“</div>
      </div>
    </div>
  </section>

  <section class="contact" role="img" aria-label="Soft photo of stacked stones and bamboo on raked sand">
    <h2 class="serif">Contact Us</h2>
    <p class="lede">Acupuncture &amp; Chinese Herbal Medicine are rooted in over 3000 years of history and tradition. As a complete medical system that has remained flexible</p>
    <div class="map" role="img" aria-label="Street map showing the clinic location"></div>
    <div class="form">
      <div class="field">Name</div>
      <div class="field">Email</div>
      <div class="field">Subject</div>
      <div class="field message">Message</div>
      <div class="submit">SUBMIT</div>
    </div>
  </section>

  <footer class="footer">
    <div class="logo">
      <div class="logo-dot"></div>
      <div><div class="logo-name">Willowgate</div><div class="logo-sub">ACUPUNCTURE</div></div>
    </div>
    <p class="about-text">Consultations are always available to help answer any questions you may have about acupuncture or herbal medicine in a relaxed environment.<br>413-555-0142</p>
    <div class="socials"><span></span><span></span><span></span><span></span><span></span></div>
    <div class="col contact-col">
      <h4>Contact</h4>
      <div class="row"><svg viewBox="0 0 8 10"><path fill="#c4939a" d="M4 0a4 4 0 0 1 4 4c0 3-4 6-4 6S0 7 0 4a4 4 0 0 1 4-4z"/></svg><span>48 Alder Row,<br>Easthaven, MA 01077,<br>USA</span></div>
      <div class="row"><svg viewBox="0 0 10 10"><circle cx="5" cy="5" r="5" fill="#c4939a"/><path d="M5 2v3h2" stroke="#1e1e20" fill="none"/></svg><span>Tuesday – Friday 10-6<br>Saturday 10-3</span></div>
    </div>
    <div class="col consult-col">
      <h4>Consultation</h4>
      <div>For questions or to schedule a FREE 30 MINUTE CONSULT</div>
      <a>maren@willowgateneedlework.com</a>
      <div>For your first visit please take some time to fill out the following new patient paper work.</div>
    </div>
    <div class="copyright">Copyrights © 2021. All rights reserved.</div>
  </footer>
</div>
</body>
</html>
```